Webdesign für TEM GmbH
Zielgruppe
TEM GmbH - Spezialist für Anlasser und Lichtmaschinen
Gegründet 1992 ist TEM nunmehr ein deutschlandweit agierendes Unternehmen mit 13 Mitarbeitern. Der Fokus unserer Arbeit liegt dabei auf der professionellen Regenerierung von Anlassern und Lichtmaschinen. Die strikte Arbeit nach Herstellerstandards und der hohe Anspruch an Qualität und Qualitätssicherung wurde durch die Einführung der ISO Zertifizierung 9001 untermauert.
Der Vertrieb von:
Anlassern
Lichtmaschinen
Turboladern
Klimakompressoren
Verdampfern / Kondensatoren
Batterien
namenhafter Hersteller ergänzt das Portfolio. Die Spezialisierung auf diese Produktgruppen ermöglicht dabei ein hohes Maß an Verfügbarkeit und marktgerechte Preise.
- Modern
- Klares und übersichtliches Desgin
- Nicht zu verspielt
- Informativ
- Leichte Navigation
- Das Design der alten Webseite soll NICHT kopiert werden
- Die Farben des Logos sollen sich wiederfinden

```html
<!DOCTYPE html>
<html lang="de">
<head>
<meta charset="utf-8">
<title>TEM GmbH – Spezialist für Anlasser und Lichtmaschinen</title>
<link href="https://fonts.googleapis.com/css2?family=Outfit:wght@300;400;500;600;700;800&display=swap" rel="stylesheet">
<style>
:root{
  --green:#00773c;
  --green-bright:#009a4e;
  --mint:#effcf7;
  --grey-bg:#f3f3f3;
  --text:#3c3c3c;
  --muted:#6a6a6a;
  --white:#ffffff;
}
*{box-sizing:border-box;margin:0;padding:0}
html,body{width:1200px;height:3004px;overflow:hidden}
body{font-family:"Outfit",sans-serif;color:var(--text);background:var(--white);position:relative}
.abs{position:absolute}
a{color:inherit;text-decoration:none}

/* hero */
.hero{position:absolute;left:0;top:0;width:1200px;height:864px;background:var(--mint)}
.topbar{position:absolute;top:18px;right:206px;display:flex;gap:18px;align-items:center;font-size:10px;color:var(--muted)}
.topbar span{display:flex;align-items:center;gap:5px}
.social-square{width:15px;height:15px;border-radius:3px;background:#7a7a7a}
.brand{position:absolute;left:206px;top:52px;display:flex;align-items:center;gap:8px;font-size:24px;font-weight:700;color:var(--green)}
.brand-dot{width:14px;height:14px;border-radius:50%;background:var(--green)}
.nav{position:absolute;top:60px;left:467px;display:flex;gap:22px;font-size:13px;font-weight:600;color:#4d5a52}
.nav .active{color:var(--green);border-bottom:2px solid var(--green);padding-bottom:4px}
.shop-btn{position:absolute;left:899px;top:49px;width:95px;height:38px;border-radius:20px;background:var(--white);box-shadow:0 6px 18px rgba(0,80,40,.12);display:flex;align-items:center;justify-content:center;gap:7px;font-size:13px;font-weight:700;color:var(--green)}
.slide-img{position:absolute;left:296px;top:128px;width:620px;height:316px;border-radius:20px;background:radial-gradient(ellipse at 50% 50%,#9aa3a6 0%,#6d7376 35%,rgba(239,252,247,0) 70%)}
.arrow{position:absolute;top:278px}
.slide-card{position:absolute;left:677px;top:264px;width:268px;height:177px;background:rgba(255,255,255,.94);border-radius:12px;box-shadow:0 20px 40px rgba(0,90,50,.12);padding:30px 37px}
.slide-card h3{font-size:27px;font-weight:700;color:var(--green);margin-bottom:12px}
.slide-card p{font-size:14px;font-weight:300;color:var(--muted);line-height:19px}
.slide-card p b{font-weight:700;color:#555}
.slide-card .more{display:flex;align-items:center;gap:7px;margin-top:16px;font-size:12px;font-weight:600;color:#2b3a31;text-decoration:underline}
.headline{position:absolute;left:206px;top:514px;line-height:62px;color:var(--green);font-weight:700;font-size:64px;letter-spacing:-1px}
.headline .thin{font-weight:300;font-size:42px;color:#4d5a52;letter-spacing:0}
.intro{position:absolute;left:206px;top:658px;width:790px;font-size:14px;font-weight:300;line-height:28.2px;color:#444}

/* band */
.band{position:absolute;left:0;top:864px;width:1200px;height:407px;background:linear-gradient(180deg,#107a45 0%,#078a4a 60%,#049451 100%);text-align:center;color:var(--white)}
.band h2{margin-top:81px;font-size:62px;font-weight:700;letter-spacing:-1px}
.band ul{list-style:none;margin-top:20px;font-size:14px;font-weight:700;line-height:28.2px}

/* video */
.video-wrap{position:absolute;left:0;top:1271px;width:1200px;height:507px;background:var(--mint)}
.video{position:absolute;left:206px;top:99px;width:491px;height:305px;border-radius:10px;background:linear-gradient(135deg,#5a5f66 0%,#8d9399 45%,#d6dbe0 70%,#3e6b4d 100%)}
.play{position:absolute;left:216px;top:133px;width:60px;height:42px;border-radius:12px;background:var(--green-bright)}
.video-text{position:absolute;left:742px;top:113px;width:270px;font-size:14px;font-weight:300;line-height:28.2px;color:#444}
.video-text strong{display:block;margin-top:20px;font-weight:700;line-height:21px;color:#111}
.btn{position:absolute;left:742px;top:346px;width:144px;height:36px;border-radius:20px;background:var(--white);box-shadow:0 6px 18px rgba(0,80,40,.12);display:flex;align-items:center;justify-content:center;gap:7px;font-size:12px;font-weight:700;color:var(--green)}

/* products */
.products{position:absolute;left:0;top:1778px;width:1200px;height:784px;background:var(--grey-bg)}
.products .kicker{position:absolute;left:204px;top:84px;font-size:42px;font-weight:300;color:#4d5a52}
.products h2{position:absolute;left:204px;top:126px;font-size:62px;font-weight:700;color:var(--green);letter-spacing:-1px}
.products .lead{position:absolute;left:206px;top:208px;width:420px;font-size:14px;font-weight:300;line-height:20px;color:#444}
.products .all{position:absolute;right:206px;top:229px;font-size:12px;font-weight:700;color:#1e2a22;display:flex;align-items:center;gap:5px}
.card{position:absolute;width:248px;background:var(--white);border-radius:8px;padding:20px 20px}
.card .icon{width:40px;height:40px;border-radius:6px;background:#f1fbf6;display:flex;align-items:center;justify-content:center;margin-bottom:10px}
.card h3{font-size:14px;font-weight:700;color:#222;margin-bottom:6px}
.card p{font-size:11px;font-weight:300;line-height:16px;color:#555}
.card ul{list-style:none;margin-top:10px;font-size:11px;font-weight:300;color:#555;line-height:19px}
.card li{display:flex;align-items:center;gap:5px}

/* footer */
.footer{position:absolute;left:0;top:2562px;width:1200px;height:341px}
.fcol{position:absolute;top:86px;font-size:11.5px;font-weight:300;color:#666}
.fcol h4{font-size:14px;font-weight:600;color:#333;margin-bottom:8px}
.fcol h4::after{content:"";display:block;width:16px;height:2px;background:#ccc;margin-top:7px}
.fcol ul{list-style:none;margin-top:16px;line-height:25.6px}
.fcol .line{line-height:17px}
.fcol .contact-row{display:flex;align-items:center;gap:7px;line-height:25px}
.partner{position:absolute;left:419px;top:240px;display:flex;align-items:center;gap:8px;font-size:20px;font-weight:400;color:#333}
.partner-square{width:22px;height:22px;border-radius:4px;background:#888}
.badge{position:absolute;left:907px;width:86px;height:86px;border-radius:50%;border:5px solid #b8b8b8;background:#f4f4f4}

/* cookie */
.cookie{position:absolute;left:0;top:2903px;width:1200px;height:101px;background:var(--grey-bg)}
.cookie p{position:absolute;left:206px;top:33px;width:470px;font-size:9.5px;line-height:12.5px;color:#444}
.cookie p span{text-decoration:underline;font-style:italic}
.cbtn{position:absolute;top:33px;height:38px;border-radius:20px;background:var(--white);display:flex;align-items:center;justify-content:center;font-size:12px;font-weight:700}
</style>
</head>
<body>

<section class="hero">
  <div class="topbar">
    <span><svg width="10" height="13" viewBox="0 0 10 13"><path d="M5 0a5 5 0 0 0-5 5c0 3.5 5 8 5 8s5-4.5 5-8a5 5 0 0 0-5-5zm0 7a2 2 0 1 1 0-4 2 2 0 0 1 0 4z" fill="#00773c"/></svg>Lindenauer Straße 42, 09111 Mittelfeld</span>
    <span><svg width="12" height="12" viewBox="0 0 12 12"><path d="M2.5 0.5l2 2.5-1.2 1.4c.8 1.6 2 2.8 3.6 3.6L8.3 6.8l2.6 2-1 2.4C5 11 1 7 .6 2z" fill="#00773c"/></svg>03721 - 48 25 3-0</span>
    <div class="social-square"></div>
  </div>
  <div class="brand"><div class="brand-dot"></div>TEM GmbH</div>
  <nav class="nav">
    <a class="active">Start</a><a>Unternehmen</a><a>Produkte</a><a>Instandsetzung</a><a>Kontakt</a>
  </nav>
  <a class="shop-btn"><svg width="15" height="13" viewBox="0 0 15 13"><path d="M0 1h2.5l2 7.5h8l2-5.5H4" fill="none" stroke="#00773c" stroke-width="1.6"/><circle cx="5.5" cy="11.5" r="1.3" fill="#00773c"/><circle cx="11" cy="11.5" r="1.3" fill="#00773c"/></svg>Shop</a>

  <div class="slide-img" role="img" aria-label="Explosionsansicht einer Lichtmaschine mit Einzelteilen"></div>
  <svg class="arrow" style="left:184px" width="22" height="40" viewBox="0 0 22 40"><path d="M19 3L4 20l15 17" fill="none" stroke="#00773c" stroke-width="5" stroke-linecap="round" stroke-linejoin="round"/></svg>
  <svg class="arrow" style="left:994px" width="22" height="40" viewBox="0 0 22 40"><path d="M3 3l15 17L3 37" fill="none" stroke="#cfeee0" stroke-width="4" stroke-linecap="round" stroke-linejoin="round"/></svg>
  <div class="slide-card">
    <h3>Anlasser</h3>
    <p>Weitere Informationen finden Sie im <b>TEM Online Shop.</b></p>
    <a class="more"><svg width="16" height="16" viewBox="0 0 16 16"><circle cx="8" cy="8" r="7" fill="none" stroke="#00773c" stroke-width="1.3"/><path d="M4.5 8h6M8 5.5L10.5 8 8 10.5" fill="none" stroke="#00773c" stroke-width="1.3"/></svg>mehr erfahren</a>
  </div>

  <h1 class="headline"><span class="thin">Ihr </span>Spezialist<span class="thin"> für</span><br>Anlasser<span class="thin"> und </span>Lichtmaschinen</h1>
  <p class="intro">Gegründet 1992 ist TEM nunmehr ein deutschlandweit agierendes Unternehmen mit 13 Mitarbeitern. Der Fokus unserer Arbeit liegt dabei auf der professionellen Regenerierung von Anlassern und Lichtmaschinen. Die strikte Arbeit nach Herstellerstandards und der hohe Anspruch an Qualität und Qualitätssicherung wurde durch die Einführung der ISO Zertifizierung 9001 untermauert.</p>
</section>

<section class="band" role="img" aria-label="Firmenfahrzeuge vor dem Firmengebäude, grün eingefärbt">
  <h2>Der Vertrieb von:</h2>
  <ul>
    <li>Anlassern</li><li>Lichtmaschinen</li><li>Turboladern</li><li>Klimakompressoren</li><li>Verdampfern / Kondensatoren</li><li>Batterien</li>
  </ul>
</section>

<section class="video-wrap">
  <div class="video" role="img" aria-label="Video: Mitarbeiter am Prüfstand für Lichtmaschinen">
    <div class="play"><svg style="position:absolute;left:24px;top:14px" width="13" height="14" viewBox="0 0 13 14"><path d="M0 0l13 7-13 7z" fill="#fff"/></svg></div>
  </div>
  <div class="video-text">
    namenhafter Hersteller ergänzt das Portfolio. Die Spezialisierung auf diese Produktgruppen ermöglicht dabei ein hohes Maß an Verfügbarkeit und marktgerechte Preise.
    <strong>Einen Überblick über unser Sortiment finden Sie in unserem Online Shop</strong>
  </div>
  <a class="btn"><svg width="15" height="13" viewBox="0 0 15 13"><path d="M0 1h2.5l2 7.5h8l2-5.5H4" fill="none" stroke="#00773c" stroke-width="1.6"/><circle cx="5.5" cy="11.5" r="1.3" fill="#00773c"/><circle cx="11" cy="11.5" r="1.3" fill="#00773c"/></svg>Zur Auswahl</a>
</section>

<section class="products">
  <div class="kicker">Unsere</div>
  <h2>Produktkategorien</h2>
  <p class="lead">Hochwertige Komponenten für PKW, LKW, Landmaschinen und Industrieanwendungen.</p>
  <a class="all">Alle Produkte ansehen <svg width="11" height="9" viewBox="0 0 11 9"><path d="M0 4.5h9M6 1l3.5 3.5L6 8" fill="none" stroke="#00773c" stroke-width="1.5"/></svg></a>

  <div class="card" style="left:206px;top:281px;height:216px">
    <div class="icon"><svg width="16" height="18" viewBox="0 0 16 18"><path d="M9 1L2 10h6l-1 7 7-9H8z" fill="none" stroke="#00773c" stroke-width="1.4" stroke-linejoin="round"/></svg></div>
    <h3>Anlasser</h3>
    <p>Robuste Starter für alle Fahrzeugtypen. Maximale Startkraft auch unter extremen Bedingungen.</p>
    <ul><li><svg width="10" height="8" viewBox="0 0 10 8"><path d="M1 4l3 3 5-6" fill="none" stroke="#00773c" stroke-width="1.6"/></svg>Neuteile &amp; AT-Teile</li><li><svg width="10" height="8" viewBox="0 0 10 8"><path d="M1 4l3 3 5-6" fill="none" stroke="#00773c" stroke-width="1.6"/></svg>Prüfprotokoll inklusive</li></ul>
  </div>
  <div class="card" style="left:476px;top:281px;height:216px">
    <div class="icon"><svg width="20" height="14" viewBox="0 0 20 14"><circle cx="4" cy="10" r="2.5" fill="none" stroke="#00773c" stroke-width="1.4"/><circle cx="15" cy="4" r="2.5" fill="none" stroke="#00773c" stroke-width="1.4"/><path d="M6.5 10H13M12.5 4H6" stroke="#00773c" stroke-width="1.4"/></svg></div>
    <h3>Lichtmaschinen</h3>
    <p>Leistungsstarke Generatoren für konstante Energieversorgung. Präzise gewuchtet und getestet.</p>
    <ul><li><svg width="10" height="8" viewBox="0 0 10 8"><path d="M1 4l3 3 5-6" fill="none" stroke="#00773c" stroke-width="1.6"/></svg>Hohe Ampere-Leistung</li><li><svg width="10" height="8" viewBox="0 0 10 8"><path d="M1 4l3 3 5-6" fill="none" stroke="#00773c" stroke-width="1.6"/></svg>OE-Spezifikationen</li></ul>
  </div>
  <div class="card" style="left:746px;top:281px;height:216px">
    <div class="icon"><svg width="20" height="16" viewBox="0 0 20 16"><path d="M2 5h11a2.5 2.5 0 1 0-2.5-2.5M2 9h14a2.5 2.5 0 1 1-2.5 2.5M2 13h6" fill="none" stroke="#00773c" stroke-width="1.4" stroke-linecap="round"/></svg></div>
    <h3>Turbolader</h3>
    <p>Effizienz und Leistung. Professionell instandgesetzte Turbolader für Diesel- und Benzinmotoren.</p>
    <ul><li><svg width="10" height="8" viewBox="0 0 10 8"><path d="M1 4l3 3 5-6" fill="none" stroke="#00773c" stroke-width="1.6"/></svg>Feingewuchtet</li><li><svg width="10" height="8" viewBox="0 0 10 8"><path d="M1 4l3 3 5-6" fill="none" stroke="#00773c" stroke-width="1.6"/></svg>Dichtungssätze verfügbar</li></ul>
  </div>

  <div class="card" style="left:206px;top:524px;height:168px">
    <div class="icon"><svg width="20" height="20" viewBox="0 0 20 20"><path d="M11 3a2 2 0 0 1 4 0v9a3.5 3.5 0 1 1-4 0z" fill="none" stroke="#00773c" stroke-width="1.4"/><path d="M3 4v8M1 6l2-2 2 2M1 12l2 2 2-2" fill="none" stroke="#00773c" stroke-width="1.3"/></svg></div>
    <h3>Klimakompressoren</h3>
    <p>Für ein optimales Klima. Neue und wiederaufbereitete Kompressoren höchster Güte.</p>
  </div>
  <div class="card" style="left:476px;top:524px;height:168px">
    <div class="icon"><svg width="22" height="12" viewBox="0 0 22 12"><rect x="1" y="1" width="17" height="10" rx="2" fill="none" stroke="#00773c" stroke-width="1.4"/><path d="M20 4v4M5 4v4M8 4v4M11 4v4" stroke="#00773c" stroke-width="1.4"/></svg></div>
    <h3>Batterien</h3>
    <p>Starterbatterien und Versorgungsbatterien. Langlebig und wartungsfrei.</p>
  </div>
  <div class="card" style="left:746px;top:524px;height:168px">
    <div class="icon"><svg width="18" height="18" viewBox="0 0 18 18"><path d="M12 1.5a4 4 0 0 0-3.6 5.6L1.5 14a1.8 1.8 0 0 0 2.5 2.5l6.9-6.9A4 4 0 0 0 16.5 6l-2.5 2.5-2.5-2.5L14 3.5A4 4 0 0 0 12 1.5z" fill="none" stroke="#00773c" stroke-width="1.4" stroke-linejoin="round"/></svg></div>
    <h3>Ersatzteile</h3>
    <p>Magnete, Regler, Freiläufe und weitere Kleinteile für die Instandsetzung.</p>
  </div>
</section>

<footer class="footer">
  <div class="fcol" style="left:206px">
    <h4>Links</h4>
    <ul><li>AGB</li><li>Impressum</li><li>Datenschutzerklärung</li><li>Downloads</li><li>Sitemap</li><li>Shop</li></ul>
  </div>
  <div class="fcol" style="left:419px">
    <h4>Öffnungszeiten</h4>
    <div style="margin-top:16px" class="line">Mo-Do: 08:00 bis 17:30 Uhr</div>
    <div style="margin-top:9px" class="line">Fr.: &nbsp;08:00 bis 17:00 Uhr<br>Sa.: &nbsp;nach Vereinbarung</div>
  </div>
  <div class="partner"><div class="partner-square"></div>PartsLink</div>
  <div class="fcol" style="left:674px">
    <h4>Kontakt</h4>
    <div style="margin-top:16px" class="line">TEM GmbH<br>Lindenauer Straße 42<br>09111 Mittelfeld</div>
    <div style="margin-top:18px">
      <div class="contact-row"><svg width="13" height="10" viewBox="0 0 13 10"><rect width="13" height="10" rx="1" fill="#777"/><path d="M0 1l6.5 4.5L13 1" fill="none" stroke="#fff" stroke-width="1"/></svg>verkauf@tem-technik.de</div>
      <div class="contact-row"><svg width="12" height="12" viewBox="0 0 12 12"><path d="M2.5 0.5l2 2.5-1.2 1.4c.8 1.6 2 2.8 3.6 3.6L8.3 6.8l2.6 2-1 2.4C5 11 1 7 .6 2z" fill="#777"/></svg>+49 (0) 3721 - 48 25 3-0</div>
      <div class="contact-row"><svg width="13" height="12" viewBox="0 0 13 12"><rect x="0" y="3" width="13" height="9" rx="1" fill="#777"/><rect x="3" y="0" width="7" height="4" fill="#777"/></svg>+49 (0) 3721 - 48 25 3-17</div>
    </div>
  </div>
  <div class="badge" style="top:80px"></div>
  <div class="badge" style="top:180px"></div>
</footer>

<div class="cookie">
  <p>Diese Website benutzt Cookies für die Authentifizierung, Navigation und andere Funktionen. Wenn Sie diese Seite weiter benutzen, stimmen Sie der Verwendung von Cookies zu.<br><span>Datenschutzerklärung anzeigen</span></p>
  <a class="cbtn" style="left:728px;width:126px;color:var(--green)">Ich stimme zu</a>
  <a class="cbtn" style="left:866px;width:128px;color:#333">Ich lehne ab</a>
</div>

</body>
</html>
```